High Quality Business card for Property Management Agency - Super Classy and professional design

High Quality Business card design.

We need a business card designed for our Property Management Agency.
We are located on Sydney's Northern Beaches and manage beautiful properties along the beach and harbor.
We need a design that oozes modern, classy and professional.
I would like it to be double sided with contact details and logo on the front and just the logo on the back.

I need a print ready PDF version of the file as well as an editable photoshop (PSD) version of the file.

Logo and information details attached.

Target Market(s)

Property owners/investors, Male and Female Aged 28-65

Industry/Entity Type

Real Estate

Contact Information for Business Card

Tom Harlow
Tel: 0437 216 590
Email: tom@harlowestates.com.au
Website: www.harlowestates.com.au
Address: Level 2, 17 Kestrel Rd, Wendale NSW 2081

Font styles to use
Sans Serif

Requirements
Must have
• - Logo front and back
• - Business card details listed above and attached
• - Colour
Nice to have
• Sleek and professional

```html
<!DOCTYPE html>
<html lang="en">
<head>
<meta charset="utf-8">
<title>Harlow Estates – Business Card</title>
<link rel="stylesheet" href="https://fonts.googleapis.com/css2?family=Open+Sans:wght@400;600;700&display=swap">
<style>
  :root {
    --bg: #2a2b2d;
    --card-white: #ffffff;
    --card-dark: #141a1c;
    --teal: #2b949c;
    --ink: #1a1a1a;
    --ink-soft: #222;
  }
  html, body {
    margin: 0;
    width: 1200px;
    height: 896px;
    overflow: hidden;
    background: var(--bg);
    font-family: "Open Sans", Arial, sans-serif;
  }
  .canvas { position: relative; width: 1200px; height: 896px; }

  .card { position: absolute; overflow: hidden; box-shadow: 0 10px 30px rgba(0,0,0,.45); }

  /* Back side */
  .card--back {
    left: 460px; top: 50px; width: 600px; height: 343px;
    background: var(--card-dark);
  }
  .card--back .brand {
    position: absolute; left: 0; right: 0; top: 120px;
    display: flex; justify-content: center; align-items: center; gap: 14px;
  }
  .brand__dot { width: 16px; height: 16px; border-radius: 50%; background: var(--teal); }
  .brand__name {
    font-weight: 700; font-size: 38px; letter-spacing: -0.5px; text-transform: uppercase;
  }
  .card--back .brand__name { color: #fff; }
  .card--back .web-row {
    position: absolute; left: 30px; right: 30px; top: 228px;
    display: flex; align-items: center; gap: 16px;
  }
  .web-row__rule { flex: 1; height: 2px; background: var(--teal); }
  .web-row__url { color: var(--teal); font-size: 18px; letter-spacing: .3px; }

  /* Front side */
  .card--front {
    left: 90px; top: 440px; width: 700px; height: 400px;
    background: var(--card-white);
  }
  .card--front .brand {
    position: absolute; left: 36px; top: 58px;
    display: flex; align-items: center; gap: 14px;
  }
  .card--front .brand__name { color: var(--ink); font-size: 40px; }
  .divider {
    position: absolute; left: 30px; top: 160px; width: 450px; height: 2px; background: var(--ink);
  }
  .contact {
    position: absolute; left: 36px; top: 178px;
    font-size: 17px; line-height: 25px; color: var(--ink-soft);
  }
  .contact p { margin: 0; }
  .contact__item { display: flex; align-items: center; gap: 8px; }
  .contact__item svg { width: 18px; height: 14px; fill: var(--ink); }
  .contact__address { margin-bottom: 6px !important; }

  .person {
    position: absolute; right: 36px; top: 232px; text-align: right;
  }
  .person__name { margin: 0; color: var(--teal); font-weight: 700; font-size: 24px; line-height: 28px; }
  .person__role { margin: 0; color: var(--ink); font-size: 18px; line-height: 24px; }
  .person__rule { height: 3px; background: var(--teal); margin-top: 4px; width: 250px; margin-left: auto; }

  .footer-strip {
    position: absolute; left: 0; top: 360px; width: 280px; height: 12px; background: var(--ink);
  }
  .footer-band {
    position: absolute; left: 250px; right: 0; bottom: 0; height: 72px;
    background: var(--teal); border-top-left-radius: 46px;
    display: flex; align-items: center; padding-left: 60px;
  }
  .footer-band__url { color: #fff; font-size: 24px; letter-spacing: .3px; }
</style>
</head>
<body>
<main class="canvas">

  <section class="card card--back" aria-label="Card back">
    <div class="brand">
      <span class="brand__dot"></span>
      <span class="brand__name">Harlow Estates</span>
    </div>
    <div class="web-row">
      <span class="web-row__rule"></span>
      <span class="web-row__url">www.harlowestates.com.au</span>
      <span class="web-row__rule"></span>
    </div>
  </section>

  <section class="card card--front" aria-label="Card front">
    <div class="brand">
      <span class="brand__name">Harlow Estates</span>
      <span class="brand__dot"></span>
    </div>
    <div class="divider"></div>

    <div class="contact">
      <p class="contact__address">Level 2, 17 Kestrel Rd,<br>Wendale NSW 2081</p>
      <p class="contact__item">
        <svg viewBox="0 0 18 14" aria-hidden="true"><path d="M2 4c0-2 3-3 7-3s7 1 7 3v2h-3V4.5C12 4 10.5 3.8 9 3.8S6 4 5 4.5V6H2z M4 7h10l2 6H2z"/></svg>
        0437 216 590
      </p>
      <p class="contact__item">
        <svg viewBox="0 0 18 14" aria-hidden="true"><path d="M1 1h16v12H1z M2.5 2.5 9 8l6.5-5.5" fill="none" stroke="#1a1a1a" stroke-width="1.6"/><path d="M1 1h16L9 8z"/></svg>
        tom@harlowestates.com.au
      </p>
    </div>

    <div class="person">
      <p class="person__name">Tom Harlow</p>
      <p class="person__role">Director/Property Manager</p>
      <div class="person__rule"></div>
    </div>

    <div class="footer-strip"></div>
    <div class="footer-band">
      <span class="footer-band__url">www.harlowestates.com.au</span>
    </div>
  </section>

</main>
</body>
</html>
```